BUsiness Card

We need a unique business card design for a new aesthetic practice, Meadowlark Skin & Vitality, P.A. The reverse of the card should be an appointment card.

```html
<!DOCTYPE html>
<html lang="en">
<head>
<meta charset="utf-8">
<title>Meadowlark Skin &amp; Vitality – Business &amp; Appointment Card</title>
<link rel="stylesheet" href="https://fonts.googleapis.com/css2?family=Quattrocento:wght@400;700&family=Marcellus&family=Fira+Sans:wght@500&display=swap">
<style>
  :root {
    --navy: #2a4d6b;
    --teal: #3fa596;
    --teal-soft: #49b0a0;
    --paper: #f5f5f3;
    --ink: #3b4250;
    --stage: #b9b9b9;
    --white: #ffffff;
  }
  * { box-sizing: border-box; margin: 0; padding: 0; }
  html, body { width: 1200px; height: 576px; overflow: hidden; }
  body {
    background: var(--stage);
    font-family: "Quattrocento", Georgia, serif;
    color: var(--ink);
    position: relative;
  }
  .card {
    position: absolute;
    top: 138px;
    height: 294px;
    background: var(--paper);
    border-radius: 12px;
    overflow: hidden;
  }
  .card--appointment { left: 82px; width: 484px; }
  .card--contact { left: 602px; width: 482px; }

  /* Brand lockup */
  .brand { position: absolute; display: flex; align-items: center; gap: 10px; }
  .brand__dot { width: 46px; height: 46px; border-radius: 50%; background: var(--navy); flex: none; }
  .brand__name {
    font-family: "Quattrocento", Georgia, serif;
    font-weight: 700;
    color: var(--navy);
    font-size: 21px;
    line-height: 1.05;
  }
  .card--appointment .brand { left: 29px; top: 30px; }
  .card--contact .brand { right: 20px; top: 28px; }
  .card--contact .brand__name { text-align: right; }

  /* Appointment side */
  .appointment-tab {
    position: absolute; right: 0; top: 0; width: 194px; height: 89px;
    background: linear-gradient(90deg, var(--teal) 0%, var(--navy) 100%);
    clip-path: polygon(0 0, 100% 0, 100% 100%, 10% 100%);
    color: var(--white);
    font-family: "Fira Sans", Arial, sans-serif;
    font-weight: 500;
    font-size: 18px;
    line-height: 23px;
    text-align: center;
    padding: 24px 0 0 24px;
  }
  .field {
    position: absolute; left: 31px; right: 32px;
    display: flex; align-items: flex-end; gap: 6px;
    font-size: 14px;
  }
  .field__line { flex: 1; border-bottom: 1px solid var(--teal); height: 1px; margin-bottom: 3px; }
  .field--name { top: 110px; }
  .field--date { top: 142px; }
  .field--time { top: 173px; }
  .weekdays {
    position: absolute; left: 30px; right: 32px; top: 211px;
    display: flex; justify-content: space-between;
    list-style: none; font-size: 14px;
  }
  .weekdays li { display: flex; align-items: center; gap: 7px; }
  .weekdays li::before {
    content: ""; width: 11px; height: 11px; border: 1px solid var(--teal);
  }
  .notice {
    position: absolute; left: 0; right: 0; bottom: 0; height: 51px;
    background: linear-gradient(90deg, var(--teal) 0%, var(--navy) 100%);
    color: var(--white);
    font-size: 13px; line-height: 16px;
    text-align: center; padding-top: 10px;
  }

  /* Contact side */
  .brand-field {
    position: absolute; left: 0; top: 0; width: 234px; height: 100%;
    background: radial-gradient(circle at 0% 55%, var(--teal-soft) 0%, var(--navy) 70%);
    clip-path: ellipse(100% 62% at 0% 55%);
  }
  .person { position: absolute; right: 20px; top: 128px; text-align: right; }
  .person__name {
    font-family: "Marcellus", Georgia, serif;
    font-size: 21px; color: var(--navy); letter-spacing: 1px;
  }
  .person__role { font-size: 12px; color: var(--teal); margin-top: 2px; }
  .contacts {
    position: absolute; right: 20px; top: 200px;
    list-style: none; text-align: right; font-size: 13px; line-height: 17px;
  }
  .contacts li { display: flex; justify-content: flex-end; align-items: center; gap: 9px; }
  .contacts svg { width: 11px; height: 11px; fill: var(--teal); flex: none; }
  .contacts .contacts__address { margin-top: 9px; }
</style>
</head>
<body>

<section class="card card--appointment">
  <div class="brand">
    <span class="brand__dot"></span>
    <span class="brand__name">Meadowlark<br>Skin &amp; Vitality</span>
  </div>
  <div class="appointment-tab">Your<br>Appointment</div>

  <div class="field field--name"><span>Name</span><span class="field__line"></span></div>
  <div class="field field--date"><span>Date</span><span class="field__line"></span></div>
  <div class="field field--time"><span>Time</span><span class="field__line"></span></div>

  <ul class="weekdays">
    <li>Mon</li><li>Tue</li><li>Wed</li><li>Thu</li><li>Fri</li><li>Sat</li>
  </ul>

  <p class="notice">If you are unable to come to the appointment.<br>Please inform us at least 2 days before.</p>
</section>

<section class="card card--contact">
  <div class="brand-field" role="img" aria-label="Large brand decoration in navy and teal"></div>

  <div class="brand">
    <span class="brand__dot"></span>
    <span class="brand__name">Meadowlark<br>Skin &amp; Vitality</span>
  </div>

  <div class="person">
    <p class="person__name">ELENA WARD</p>
    <p class="person__role">Managing Director</p>
  </div>

  <ul class="contacts">
    <li>555.010.2478
      <svg viewBox="0 0 24 24" aria-hidden="true"><path d="M6.6 10.8a15 15 0 0 0 6.6 6.6l2.2-2.2a1 1 0 0 1 1-.25 11.4 11.4 0 0 0 3.6.57 1 1 0 0 1 1 1V20a1 1 0 0 1-1 1A17 17 0 0 1 3 4a1 1 0 0 1 1-1h3.5a1 1 0 0 1 1 1c0 1.25.2 2.45.57 3.6a1 1 0 0 1-.25 1z"/></svg>
    </li>
    <li>elena@meadowlarkskin.com
      <svg viewBox="0 0 24 24" aria-hidden="true"><path d="M2 5h20v14H2z M2 5l10 8 10-8" stroke="#f5f5f3" stroke-width="1.6"/></svg>
    </li>
    <li>www.meadowlarkskin.com
      <svg viewBox="0 0 24 24" aria-hidden="true"><path d="M12 2a10 10 0 1 0 0 20 10 10 0 0 0 0-20zm0 2c1.4 1.6 2.3 4.2 2.4 7H9.6c.1-2.8 1-5.4 2.4-7zM4.1 11a8 8 0 0 1 3.8-6 13 13 0 0 0-2.3 6zm0 2h3.5a13 13 0 0 0 2.3 6 8 8 0 0 1-5.8-6zm5.5 0h4.8c-.1 2.8-1 5.4-2.4 7-1.4-1.6-2.3-4.2-2.4-7zm6.8 0h3.5a8 8 0 0 1-5.8 6 13 13 0 0 0 2.3-6zm0-2a13 13 0 0 0-2.3-6 8 8 0 0 1 5.8 6z"/></svg>
    </li>
    <li class="contacts__address">87 Harbor Lane, Fairview, US 10452</li>
  </ul>
</section>

</body>
</html>
```